Non Profit Company Looking For New Website

The website for Corvale Paddock Rehoming Society should offer the viewer beautiful photos that inspire condifence and joy and tap into our love of horses.

We would like to see a website that displays trust, quality and confidence. Needs to be responsive and mobile friendly for all browsers and coded for both Android & IOS.

READ ATTACHED WEBSITE TEMPLATE FOR COMPLETE DETAILS ON WHAT WE ARE LOOKING FOR.

Looking for recommmendations if we should use WordPress/WooCommerce for site or Wordpress with Shopify Plug in or just Shopify.

Must be both desktop and mobile friendly with fast page load speed. Need the ability to edit ourselves.

Industry/Entity Type

Non Profit

Coding

Coded - Design and coding required

Number of Pages Required

5+ page

Requirements
Must have
• We would like to see a website that displays trust, quality and confidence. Needs to be responsive and mobile friendly for all browsers and coded for both Android & IOS.

Looking for recommendations if we should use WordPress/WooCommerce for site or Wordpress with Shopify Plug in or just Shopify.

Logo Colour:
Pantone 7621 C

READ TEMPLATE THAT IS ATTACHED
Nice to have
• Like look of this website as a sample:
https://www.quillmanegallop.com/

Another similar non profit organization
https://brindlefieldrest.com/

```html
<!DOCTYPE html>
<html lang="en">
<head>
<meta charset="utf-8">
<title>Corvale Paddock Rehoming Society</title>
<link href="https://fonts.googleapis.com/css2?family=Poppins:wght@400;500;600;700&family=Cinzel:wght@400&display=swap" rel="stylesheet">
<style>
:root{
  --red:#c11f2e;
  --red-dark:#a81a27;
  --ink:#1b1b1b;
  --text:#3a3a3a;
  --muted:#777;
  --line:#d9d9d9;
  --white:#ffffff;
  --black:#111111;
}
*{box-sizing:border-box;margin:0;padding:0}
html,body{width:1200px;height:2841px;overflow:hidden}
body{position:relative;background:var(--white);font-family:"Poppins",sans-serif;color:var(--text)}
.abs{position:absolute}

/* header */
.site-header{position:absolute;left:0;top:0;width:1200px;height:126px;background:var(--white)}
.brand{position:absolute;left:120px;top:14px;width:124px;text-align:center;font-family:"Cinzel",serif;color:var(--red);line-height:1.1}
.brand .mark{display:block;width:30px;height:30px;margin:6px auto 5px;border-radius:50%;background:var(--red)}
.brand .top{font-size:18px}
.brand .sub{font-size:11px}
.main-nav a{position:absolute;top:54px;font-size:14.5px;color:var(--ink);text-decoration:none}
.main-nav a.active{color:var(--red);font-weight:500}

/* photo bands */
.hero{left:0;top:126px;width:1200px;height:582px;
  background:
    radial-gradient(ellipse 22% 40% at 38% 55%,rgba(60,40,30,.45),rgba(60,40,30,0) 70%),
    radial-gradient(ellipse 35% 38% at 75% 55%,rgba(120,60,25,.55),rgba(120,60,25,0) 70%),
    linear-gradient(180deg,rgba(40,60,30,.55) 0%,rgba(40,60,30,.15) 30%,rgba(0,0,0,0) 45%,rgba(0,0,0,.05) 100%),
    linear-gradient(90deg,#d2a448 0%,#b3a546 18%,#7f9d43 38%,#6b9440 60%,#5c8a3a 80%,#6f8c44 100%)}
.adopt{left:0;top:1357px;width:1200px;height:636px;
  background:
    radial-gradient(ellipse 45% 55% at 18% 60%,rgba(20,14,10,.95),rgba(20,14,10,0) 75%),
    radial-gradient(ellipse 28% 30% at 85% 25%,rgba(70,120,60,.7),rgba(70,120,60,0) 75%),
    radial-gradient(ellipse 25% 25% at 60% 55%,rgba(180,120,100,.35),rgba(180,120,100,0) 70%),
    linear-gradient(90deg,#2a221c 0%,#3a3228 30%,#3f5636 55%,#3b6a3c 78%,#2e5a33 100%)}
.chevron{position:absolute;left:590px;width:20px;height:12px}

/* intro */
.intro-title{left:150px;top:738px;width:900px;text-align:center;font-size:21px;font-weight:600;color:var(--black);line-height:1.4;text-transform:uppercase}
.intro-sub{left:150px;top:800px;width:900px;text-align:center;font-size:14.5px;color:var(--red)}

/* about */
.about-title{left:129px;top:956px;font-size:18px;font-weight:600;color:var(--black)}
.about-text{left:129px;top:996px;width:458px;font-size:13px;line-height:26px;text-align:justify;color:var(--text)}
.btn{position:absolute;display:flex;align-items:center;justify-content:center;font-size:14px;font-weight:500;text-transform:uppercase;border-radius:3px;text-decoration:none}
.btn-red{background:var(--red);color:var(--white)}
.btn-outline{border:1.5px solid var(--white);color:var(--white)}
.about-photo{left:712px;top:930px;width:334px;height:334px;border-radius:50%;
  background:radial-gradient(circle at 35% 40%,#6e3f24 0%,#5a3522 28%,#6c5a44 45%,#9fae8c 65%,#e3e5df 85%)}

/* adopt text */
.adopt-title{left:0;top:1615px;width:1200px;text-align:center;font-size:18px;font-weight:600;color:var(--white);text-transform:uppercase}
.adopt-text{left:0;top:1643px;width:1200px;text-align:center;font-size:14px;color:var(--white)}

/* contact */
.section-head{font-size:18px;font-weight:600;color:var(--black);text-transform:uppercase}
.section-head span{color:var(--red)}
.head-rule{height:2px;width:30px;background:var(--line)}
.info-icon{width:52px;height:52px;border-radius:50%;background:var(--red);display:flex;align-items:center;justify-content:center}
.info-label{font-size:13.5px;font-weight:600;color:var(--black);text-transform:uppercase}
.info-value{font-size:11.5px;color:var(--text);line-height:18px}
.contact-intro{left:598px;top:2126px;font-size:14px;line-height:21px;color:var(--text)}
.field{position:absolute;border:1px solid var(--line);border-radius:2px;display:flex;align-items:flex-start;font-size:12px;color:var(--muted)}
.field .ico{width:36px;height:34px;border-right:1px solid var(--line);display:flex;align-items:center;justify-content:center;flex-shrink:0}
.field .ph{padding:10px 0 0 11px}
.captcha{left:599px;top:2400px;width:204px;height:51px;border:1px solid var(--line);background:#f9f9f9;border-radius:2px}
.captcha .box{position:absolute;left:14px;top:14px;width:22px;height:22px;border:2px solid #c1c1c1;background:var(--white);border-radius:2px}
.captcha .lbl{position:absolute;left:42px;top:17px;font-size:11px;font-weight:500;color:var(--black)}
.captcha .seal{position:absolute;right:14px;top:12px;width:24px;height:24px;background:#c9d6ea;border-radius:4px}

/* footer */
.site-footer{left:0;top:2612px;width:1200px;height:195px;background:var(--red);color:var(--white)}
.foot-brand{left:129px;top:2640px;width:139px;text-align:center;font-family:"Cinzel",serif;color:var(--white);line-height:1.15}
.foot-brand .top{font-size:24px}
.foot-brand .mark{display:block;width:40px;height:40px;margin:8px auto;border-radius:50%;border:2px solid var(--white)}
.foot-brand .sub{font-size:14px}
.foot-head{font-size:12.5px;font-weight:600;text-transform:uppercase;color:var(--white)}
.foot-links{font-size:11px;line-height:18px;color:var(--white)}
.foot-rule{width:1px;height:130px;background:rgba(255,255,255,.45)}
.social{width:24px;height:24px;border:1.5px solid var(--white);border-radius:50%}
.foot-input{border:1px solid var(--white);border-radius:2px;font-size:11px;padding:6px 10px;height:26px;color:var(--white)}
.copyright{left:0;top:2807px;width:1200px;height:34px;background:var(--black);color:#cfcfcf;font-size:9.5px;display:flex;align-items:center;justify-content:center}
</style>
</head>
<body>

<header class="site-header">
  <div class="brand">
    <div class="top">CORVALE</div>
    <span class="mark"></span>
    <div class="sub">PADDOCK<br>REHOMING</div>
  </div>
  <nav class="main-nav">
    <a class="active" style="left:613px">Home</a>
    <a style="left:685px">About</a>
    <a style="left:756px">Adopt</a>
    <a style="left:827px">Horses</a>
    <a style="left:903px">Donate/Shop</a>
    <a style="left:1021px">Contact</a>
  </nav>
</header>

<div class="abs hero" role="img" aria-label="Photo of a rider in a cowboy hat greeting a saddled chestnut horse in a sunny grass field"></div>
<svg class="chevron" style="top:661px" viewBox="0 0 20 12"><path d="M1 1l9 9 9-9" fill="none" stroke="#fff" stroke-width="2"/></svg>

<h1 class="abs intro-title">We support and develop retired thoroughbred racehorses for<br>their next chapter in life retire. retrain. rehome.</h1>
<p class="abs intro-sub">Corvale Paddock Rehoming Society (CPRS) is a registered not-for-profit organization in Corvale Valley.</p>

<h2 class="abs about-title">WHAT IS THOROUGHBRED AFTERCARE?</h2>
<p class="abs about-text">The health, safety and welfare of our equine athletes does not end at the finish line, and retirement and aftercare are critical to the success of the racing industry. Aftercare is the safe placement of racehorses after their careers as racehorse are completed. Some horses might retire to the breeding shed or broodmare bands, while others are re-trained for second careers.</p>
<a class="btn btn-red" style="left:127px;top:1174px;width:186px;height:45px">Learn more about us</a>

<svg class="abs" style="left:690px;top:900px" width="400" height="400" viewBox="0 0 400 400">
  <path d="M230 16 A186 186 0 0 1 120 376" fill="none" stroke="#c11f2e" stroke-width="4"/>
  <path d="M250 20 A182 182 0 0 1 300 352" fill="none" stroke="#c11f2e" stroke-width="14" stroke-linecap="round"/>
</svg>
<div class="abs about-photo" role="img" aria-label="Photo of a rider on a bay horse jumping, framed in a circle"></div>
<svg class="chevron" style="top:1309px" viewBox="0 0 20 12"><path d="M1 1l9 9 9-9" fill="none" stroke="#111" stroke-width="2"/></svg>

<div class="abs adopt" role="img" aria-label="Close-up photo of a hand reaching to touch a horse's muzzle in front of green trees"></div>
<h2 class="abs adopt-title">Adopt a horse</h2>
<p class="abs adopt-text">Corvale Paddock Rehoming is committed to helping match you with the perfect horse.</p>
<a class="btn btn-outline" style="left:404px;top:1683px;width:185px;height:44px">Adopt now</a>
<a class="btn btn-red" style="left:610px;top:1683px;width:185px;height:44px">More ways to give</a>
<svg class="chevron" style="top:1771px" viewBox="0 0 20 12"><path d="M1 1l9 9 9-9" fill="none" stroke="#fff" stroke-width="2"/></svg>

<h2 class="abs section-head" style="left:127px;top:2080px"><span>Contact</span> info</h2>
<div class="abs head-rule" style="left:127px;top:2114px"></div>

<div class="abs info-icon" style="left:126px;top:2133px">
  <svg width="18" height="22" viewBox="0 0 18 22"><path d="M9 1a7 7 0 0 0-7 7c0 5 7 13 7 13s7-8 7-13a7 7 0 0 0-7-7z" fill="#fff"/><circle cx="9" cy="8" r="2.6" fill="#c11f2e"/></svg>
</div>
<div class="abs info-label" style="left:195px;top:2132px">Corvale Paddock Rehoming</div>
<div class="abs info-value" style="left:195px;top:2151px">418 Larkspur Road, Suite 12,<br>Corvale Valley, CV 20417</div>

<div class="abs info-icon" style="left:126px;top:2214px">
  <svg width="20" height="20" viewBox="0 0 20 20"><path d="M4 2l4 1 1 4-2 2a11 11 0 0 0 4 4l2-2 4 1 1 4-2 2C9 18 2 11 2 4z" fill="#fff"/></svg>
</div>
<div class="abs info-label" style="left:195px;top:2224px">Phone</div>
<div class="abs info-value" style="left:195px;top:2242px">555-0142-2288</div>

<div class="abs info-icon" style="left:126px;top:2296px">
  <svg width="22" height="16" viewBox="0 0 22 16"><rect x="1" y="1" width="20" height="14" fill="none" stroke="#fff" stroke-width="1.6"/><path d="M1 1l10 8 10-8M1 15l7-7M21 15l-7-7" fill="none" stroke="#fff" stroke-width="1.4"/></svg>
</div>
<div class="abs info-label" style="left:195px;top:2305px">Email</div>
<div class="abs info-value" style="left:195px;top:2323px">info@corvalepaddock.org</div>

<h2 class="abs section-head" style="left:598px;top:2080px"><span>Contact</span> us</h2>
<div class="abs head-rule" style="left:598px;top:2114px"></div>
<p class="abs contact-intro">Have a question or need more information?<br>Give us a call or use the form below</p>

<div class="field" style="left:599px;top:2202px;width:232px;height:36px">
  <span class="ico"><svg width="12" height="12" viewBox="0 0 12 12"><circle cx="6" cy="3.5" r="3" fill="#c11f2e"/><path d="M0 12c0-4 3-5 6-5s6 1 6 5z" fill="#c11f2e"/></svg></span><span class="ph">First Name*</span>
</div>
<div class="field" style="left:844px;top:2202px;width:231px;height:36px">
  <span class="ico"><svg width="12" height="12" viewBox="0 0 12 12"><circle cx="6" cy="3.5" r="3" fill="#c11f2e"/><path d="M0 12c0-4 3-5 6-5s6 1 6 5z" fill="#c11f2e"/></svg></span><span class="ph">Last Name*</span>
</div>
<div class="field" style="left:599px;top:2252px;width:232px;height:36px">
  <span class="ico"><svg width="12" height="12" viewBox="0 0 20 20"><path d="M4 2l4 1 1 4-2 2a11 11 0 0 0 4 4l2-2 4 1 1 4-2 2C9 18 2 11 2 4z" fill="#c11f2e"/></svg></span><span class="ph">Your Phone*</span>
</div>
<div class="field" style="left:844px;top:2252px;width:231px;height:36px">
  <span class="ico"><svg width="14" height="10" viewBox="0 0 14 10"><rect width="14" height="10" fill="#c11f2e"/><path d="M0 0l7 5 7-5" fill="none" stroke="#fff"/></svg></span><span class="ph">Your Email*</span>
</div>
<div class="field" style="left:599px;top:2302px;width:476px;height:82px">
  <span class="ico"><svg width="12" height="11" viewBox="0 0 12 11"><path d="M6 0C2.7 0 0 2 0 4.6c0 1.5.9 2.8 2.3 3.6L1.6 11l3-2.1c.4.1.9.1 1.4.1 3.3 0 6-2 6-4.6S9.3 0 6 0z" fill="#c11f2e"/></svg></span><span class="ph">Your Message*</span>
</div>

<div class="abs captcha">
  <span class="box"></span>
  <span class="lbl">I'm not a robot</span>
  <span class="seal"></span>
</div>
<a class="btn btn-red" style="left:599px;top:2467px;width:140px;height:41px">Submit</a>

<footer class="abs site-footer"></footer>
<div class="abs foot-brand">
  <div class="top">CORVALE</div>
  <span class="mark"></span>
  <div class="sub">PADDOCK<br>REHOMING</div>
</div>

<div class="abs foot-head" style="left:345px;top:2640px">Navigate</div>
<div class="abs foot-links" style="left:345px;top:2665px">Home<br>About<br>Adopt<br>Horses<br>Donate/Shop<br>Contact</div>
<div class="abs foot-rule" style="left:460px;top:2640px"></div>

<div class="abs foot-head" style="left:504px;top:2640px">Contact us</div>
<div class="abs foot-links" style="left:504px;top:2665px;padding-left:16px">(555) 014-2288<br>info@corvalepaddock.org</div>
<div class="abs foot-links" style="left:504px;top:2718px;padding-left:16px">418 Larkspur Road<br>Suite 12, Corvale Valley<br>CV 20417</div>
<svg class="abs" style="left:504px;top:2669px" width="10" height="10" viewBox="0 0 20 20"><path d="M4 2l4 1 1 4-2 2a11 11 0 0 0 4 4l2-2 4 1 1 4-2 2C9 18 2 11 2 4z" fill="#fff"/></svg>
<svg class="abs" style="left:504px;top:2689px" width="10" height="8" viewBox="0 0 14 10"><rect width="14" height="10" fill="#fff"/><path d="M0 0l7 5 7-5" fill="none" stroke="#c11f2e"/></svg>
<svg class="abs" style="left:504px;top:2722px" width="10" height="13" viewBox="0 0 18 22"><path d="M9 1a7 7 0 0 0-7 7c0 5 7 13 7 13s7-8 7-13a7 7 0 0 0-7-7z" fill="#fff"/><circle cx="9" cy="8" r="2.6" fill="#c11f2e"/></svg>
<div class="abs foot-rule" style="left:689px;top:2640px"></div>

<div class="abs foot-head" style="left:733px;top:2640px">Follow us</div>
<div class="abs social" style="left:733px;top:2670px"></div>
<div class="abs social" style="left:765px;top:2670px"></div>
<div class="abs social" style="left:796px;top:2670px"></div>
<div class="abs foot-rule" style="left:864px;top:2640px"></div>

<div class="abs foot-head" style="left:913px;top:2640px">Subscribe</div>
<div class="abs foot-input" style="left:913px;top:2670px;width:161px">Name</div>
<div class="abs foot-input" style="left:913px;top:2705px;width:161px">Email</div>
<a class="btn" style="left:913px;top:2742px;width:103px;height:28px;border:1.5px solid #fff;color:#fff;font-size:10.5px;font-weight:600">Subscribe</a>

<div class="abs copyright">Copyright © 2021 Corvale paddock rehoming. All Rights Reserved</div>

</body>
</html>
```